Looking for awesome business card design with attached existing logo

We are a water, mold, and fire damage restoration company called "Torvane Seco" Looking for an awesome business card that is edgy yet professional and unique. Show me what you got!

```html
<!DOCTYPE html>
<html lang="en">
<head>
<meta charset="utf-8">
<title>Torvane Seco – Business Card</title>
<link href="https://fonts.googleapis.com/css2?family=Montserrat:wght@400;500;700&display=swap" rel="stylesheet">
<style>
  :root {
    --backdrop: #3b3b3c;
    --teal: #0b4250;
    --teal-deep: #083c49;
    --amber: #e49b0f;
    --ink: #1f2a2e;
    --paper: #ffffff;
    --rule: #9a9a9a;
  }
  * { margin: 0; padding: 0; box-sizing: border-box; }
  html, body { width: 1200px; height: 1200px; overflow: hidden; }
  body {
    background: var(--backdrop);
    font-family: "Montserrat", sans-serif;
    position: relative;
  }
  .card {
    position: absolute;
    left: 170px;
    width: 860px;
    height: 491px;
    border-radius: 34px;
    overflow: hidden;
    box-shadow: 0 18px 40px rgba(0,0,0,0.45);
  }
  .card--front { top: 70px; background: var(--paper); }
  .card--back { top: 630px; background: var(--teal-deep); }

  .brand {
    position: absolute;
    display: flex;
    align-items: center;
    gap: 14px;
    font-weight: 700;
    letter-spacing: 1px;
    white-space: nowrap;
  }
  .brand__dot { border-radius: 50%; background: var(--amber); flex: none; }
  .card--front .brand { left: 200px; top: 120px; font-size: 48px; color: var(--teal); }
  .card--front .brand__dot { width: 22px; height: 22px; }
  .card--back .brand { left: 50%; top: 50%; transform: translate(-50%, -50%); font-size: 70px; color: var(--paper); }
  .card--back .brand__dot { width: 30px; height: 30px; }

  .holder {
    position: absolute;
    left: 62px;
    top: 340px;
    padding-left: 18px;
    border-left: 6px solid var(--amber);
  }
  .holder__name { font-size: 34px; font-weight: 500; color: var(--amber); line-height: 1; }
  .holder__role { font-size: 18px; font-weight: 400; color: var(--ink); margin-top: 4px; letter-spacing: 0.5px; }

  .divider {
    position: absolute;
    left: 470px;
    top: 250px;
    width: 1px;
    height: 90px;
    background: var(--rule);
  }

  .contact {
    position: absolute;
    left: 520px;
    top: 230px;
    list-style: none;
  }
  .contact__item {
    display: flex;
    align-items: center;
    gap: 12px;
    font-size: 21px;
    color: var(--ink);
    margin-bottom: 12px;
  }
  .contact__icon { width: 24px; height: 24px; flex: none; }

  .band { position: absolute; bottom: 0; height: 34px; }
  .band--amber { left: 0; width: 548px; background: var(--amber); }
  .band--teal { left: 560px; right: 0; background: var(--teal); }
</style>
</head>
<body>
  <section class="card card--front">
    <div class="brand"><span class="brand__dot"></span>Torvane Seco</div>

    <div class="holder">
      <p class="holder__name">JOHN DOE</p>
      <p class="holder__role">POSITION</p>
    </div>

    <div class="divider"></div>

    <ul class="contact">
      <li class="contact__item">
        <svg class="contact__icon" viewBox="0 0 24 24" fill="var(--amber)"><path d="M6.6 10.8a15.1 15.1 0 0 0 6.6 6.6l2.2-2.2a1 1 0 0 1 1-.25 11.4 11.4 0 0 0 3.6.57 1 1 0 0 1 1 1V20a1 1 0 0 1-1 1A17 17 0 0 1 3 4a1 1 0 0 1 1-1h3.5a1 1 0 0 1 1 1c0 1.25.2 2.45.57 3.57a1 1 0 0 1-.25 1z"/></svg>
        (000) 000 0000
      </li>
      <li class="contact__item">
        <svg class="contact__icon" viewBox="0 0 24 24" fill="var(--amber)"><path d="M2 5h20v14H2z M3.5 6.5 12 13l8.5-6.5" stroke="#fff" stroke-width="1.4"/></svg>
        hello@torvaneseco.com
      </li>
      <li class="contact__item">
        <svg class="contact__icon" viewBox="0 0 24 24" fill="none" stroke="var(--amber)" stroke-width="1.8"><circle cx="12" cy="12" r="9.5"/><ellipse cx="12" cy="12" rx="4" ry="9.5"/><path d="M2.5 12h19M4 7h16M4 17h16"/></svg>
        www.torvaneseco.com
      </li>
    </ul>

    <div class="band band--amber"></div>
    <div class="band band--teal"></div>
  </section>

  <section class="card card--back">
    <div class="brand"><span class="brand__dot"></span>Torvane Seco</div>
  </section>
</body>
</html>
```